"Cork Hollow Excursions" is a top notch Santa Barbara County Wine Tour company.

We provide scenic, boutique and custom wine tours. I need the card to be clean and classy. I will provide our logo. I would like the logo to cover the back side of the card as an option and would like to see a couple color options other then our signature green and gold. I would like to see some creative options and let the designers come up with options.
I need cards for myself and my team. The final design should communicate "An authentic and boutique wine tour experience"
Please use my website for reference www.corkhollowexcursions.com

Target Market(s)

We have a wide range of clients from millennials to baby boomers

Industry/Entity Type

Tour

Contact Information for Business Card

Contact info:
Dale Munford
805-291-6384
info@corkhollowexcursions.com
corkhollowexcursions.com

Colors

Designer to choose colors to be used in the design.

Requirements
Must have
• my logo
Nice to have
• *I would like to have the backside side with the logo and the company statement
• "An authentic and boutique wine tour experience" as an option.
• *I would also like to see what the designers can create!
• *I would like to see an option that incorporates or social: snapgrid, rovia, route scout
Should not have
• I do not want it too busy.

```html
<!DOCTYPE html>
<html lang="en">
<head>
<meta charset="utf-8">
<title>Cork Hollow Excursions – Business Card</title>
<link href="https://fonts.googleapis.com/css2?family=Cinzel:wght@400;500&family=Arimo:wght@400&display=swap" rel="stylesheet">
<style>
  :root {
    --backdrop: #e9e6e1;
    --night-sky: #2c3545;
    --dusk-hill: #3f3a2a;
    --vine-olive: #5c5a2c;
    --card-white: #ffffff;
    --vine-green: #2f6b47;
    --vine-green-light: #5c8f70;
    --gold: #a58d6f;
    --ink-soft: #5f6b63;
  }
  * { box-sizing: border-box; margin: 0; padding: 0; }
  html, body {
    width: 1200px; height: 930px; overflow: hidden;
    background: var(--backdrop);
  }
  .canvas { position: relative; width: 1200px; height: 930px; }

  .card {
    position: absolute;
    width: 560px; height: 320px;
    overflow: hidden;
    box-shadow: 0 6px 18px rgba(0,0,0,0.18);
  }

  /* Front side */
  .card-front { left: 140px; top: 90px; }
  .front-scene {
    position: absolute; inset: 0;
    background: linear-gradient(180deg, var(--night-sky) 0%, #3b4250 40%, var(--dusk-hill) 62%, var(--vine-olive) 80%, #3a3620 100%);
  }
  .front-brand {
    position: absolute; left: 0; right: 0; top: 118px;
    text-align: center; color: var(--card-white);
  }
  .front-brand .brand-name {
    font-family: "Cinzel", serif; font-weight: 500;
    font-size: 34px; letter-spacing: 1px; line-height: 1.1;
  }
  .front-brand .brand-region {
    font-family: "Cinzel", serif; font-size: 12px;
    letter-spacing: 6px; margin-top: 12px;
    border-top: 1px solid rgba(255,255,255,0.7);
    display: inline-block; padding-top: 8px;
  }

  /* Back side */
  .card-back { left: 500px; top: 500px; background: var(--card-white); }
  .back-rows {
    position: absolute; left: 80px; right: 0; bottom: 0; height: 200px;
    background: radial-gradient(ellipse at 35% 0%, rgba(255,255,255,1) 0%, rgba(255,255,255,0.9) 30%, rgba(92,143,112,0.55) 60%, var(--vine-green) 100%);
  }
  .back-brand {
    position: absolute; left: 28px; top: 88px; width: 250px;
    text-align: center;
  }
  .back-brand .brand-name {
    font-family: "Cinzel", serif; font-weight: 500;
    font-size: 24px; line-height: 1.15; color: var(--gold);
  }
  .back-brand .brand-region {
    font-family: "Cinzel", serif; font-size: 9px; letter-spacing: 4.5px;
    color: var(--vine-green); margin-top: 8px;
    border-top: 1px solid var(--gold); display: inline-block; padding-top: 6px;
  }
  .back-divider {
    position: absolute; left: 298px; top: 40px; width: 1px; height: 150px;
    background: var(--ink-soft); opacity: 0.6;
  }
  .contact {
    position: absolute; left: 316px; top: 38px; width: 240px;
    font-family: "Arimo", sans-serif; color: var(--ink-soft);
    font-size: 11.5px; line-height: 1.45;
  }
  .contact .person-name {
    font-family: "Cinzel", serif; font-size: 19px; color: var(--vine-green);
    line-height: 1.1;
  }
  .contact .person-role { margin-bottom: 8px; }
  .contact .address { margin-left: 12px; margin-bottom: 6px; }
  .contact .line { display: flex; align-items: center; gap: 8px; }
  .contact svg { width: 10px; height: 10px; flex: none; }
</style>
</head>
<body>
<main class="canvas">

  <section class="card card-front" aria-label="Card front">
    <div class="front-scene" role="img" aria-label="Photograph of vineyard rows on rolling hills at dusk"></div>
    <div class="front-brand">
      <div class="brand-name">Cork Hollow<br>Excursions</div>
      <div class="brand-region">SANTA BARBARA COUNTY</div>
    </div>
  </section>

  <section class="card card-back" aria-label="Card back">
    <div class="back-rows" role="img" aria-label="Decorative green vineyard rows radiating from the centre"></div>
    <div class="back-brand">
      <div class="brand-name">Cork Hollow<br>Excursions</div>
      <div class="brand-region">SANTA BARBARA COUNTY</div>
    </div>
    <div class="back-divider"></div>
    <div class="contact">
      <div class="person-name">Dale Munford</div>
      <div class="person-role">Founder</div>
      <div class="address">418 Alder Ridge Rd.<br>Fenwick, MO 63051</div>
      <div class="line">
        <svg viewBox="0 0 10 10"><path d="M2 1 L4 1 L4.6 3 L3.6 3.8 Q4.6 5.6 6.2 6.4 L7 5.4 L9 6 L9 8 Q5 9 2.5 5.5 Q1 3 2 1Z" fill="var(--ink-soft)"/></svg>
        <span>805-291-6384</span>
      </div>
      <div class="line">
        <svg viewBox="0 0 10 10"><rect x="0.8" y="2" width="8.4" height="6" fill="none" stroke="var(--ink-soft)" stroke-width="1"/><path d="M1 2.3 L5 5.5 L9 2.3" fill="none" stroke="var(--ink-soft)" stroke-width="1"/></svg>
        <span>info@corkhollowexcursions.com</span>
      </div>
      <div class="line">
        <svg viewBox="0 0 10 10"><circle cx="5" cy="5" r="4" fill="none" stroke="var(--ink-soft)" stroke-width="1"/><ellipse cx="5" cy="5" rx="1.8" ry="4" fill="none" stroke="var(--ink-soft)" stroke-width="0.8"/><line x1="1" y1="5" x2="9" y2="5" stroke="var(--ink-soft)" stroke-width="0.8"/></svg>
        <span>www.corkhollowexcursions.com</span>
      </div>
    </div>
  </section>

</main>
</body>
</html>
```